one side yoga classes, other side rental log cabin

I need a flyer to advertise yoga classes on a lake , and to describe the various styles of classes, and who they can benefit, Days Times .prices
Linked to it is a rental log cabin that can be rented privetly to families or Groups (8 max) www.staysbycalderbrook.com This also is rented to yoga teacher that would like to Hire Cabin and the Studio www.velinoretreat.co.uk or
for Holistic weekends.

Teacher

```html
<!DOCTYPE html>
<html lang="en">
<head>
<meta charset="utf-8">
<title>Velino Retreat &amp; Calderbrook Lodge Flyer</title>
<link href="https://fonts.googleapis.com/css2?family=Open+Sans:wght@400;600;700&family=Quicksand:wght@400;500&family=Arimo:wght@400;700&display=swap" rel="stylesheet">
<style>
  :root {
    --backdrop: #000000;
    --paper: #ffffff;
    --ink: #1c1c1c;
    --ink-soft: #6f6f6f;
    --accent-red: #e0262a;
    --band: #8c8584;
    --band-text: #f2efee;
    --lake-top: #ffffff;
    --lake-mid: #e4efec;
    --lake-low: #bcd6d1;
  }
  * { margin: 0; padding: 0; box-sizing: border-box; }
  html, body {
    width: 996px; height: 1200px; overflow: hidden;
    background: var(--backdrop);
  }
  .canvas { position: relative; width: 996px; height: 1200px; }
  .flyer {
    position: absolute; left: 110px; width: 758px; height: 537px;
    background: var(--paper); overflow: hidden;
    font-family: "Open Sans", Arial, sans-serif; color: var(--ink);
  }
  .flyer--yoga { top: 45px; }
  .flyer--lodge { top: 615px; }

  /* Yoga side */
  .lake-photo {
    position: absolute; inset: 0;
    background:
      radial-gradient(ellipse 40% 55% at 78% 60%, rgba(255,255,255,0.9), rgba(255,255,255,0) 70%),
      linear-gradient(180deg, var(--lake-top) 0%, var(--lake-top) 40%, var(--lake-mid) 62%, var(--lake-low) 100%);
  }
  .yoga-title {
    position: absolute; left: 30px; top: 29px;
    font-size: 19px; font-weight: 400; letter-spacing: 0.5px;
  }
  .schedule { position: absolute; left: 32px; width: 402px; font-size: 11.6px; line-height: 15px; }
  .schedule h3 { font-size: 11.6px; font-weight: 700; }
  .schedule .row { line-height: 20.5px; }
  .schedule .note { color: var(--accent-red); font-weight: 700; }
  .schedule strong { font-weight: 700; }
  .site-url {
    position: absolute; font-size: 15px; letter-spacing: 0.6px; color: var(--ink);
  }
  .site-url--retreat { left: 500px; top: 37px; width: 212px; text-align: center; }
  .brand-name {
    position: absolute; left: 468px; top: 78px; width: 250px; text-align: center;
    font-size: 30px; font-weight: 400; letter-spacing: 4px; color: var(--ink);
  }
  .info-band {
    position: absolute; left: 0; top: 449px; width: 758px; height: 88px;
    background: var(--band); color: var(--band-text);
  }
  .tagline {
    position: absolute; left: 32px; top: 23px; width: 316px; text-align: center;
    font-family: "Arimo", Arial, sans-serif; font-size: 13.5px; line-height: 15px; letter-spacing: 0.6px;
  }
  .booking { position: absolute; left: 396px; top: 12px; width: 310px; text-align: center; color: #fff; }
  .booking-lead { font-size: 19px; letter-spacing: 0.5px; line-height: 24px; }
  .booking-phone { font-family: "Arimo", Arial, sans-serif; font-size: 28px; font-weight: 700; letter-spacing: 1px; line-height: 34px; }

  /* Lodge side */
  .lodge-photo {
    position: absolute; left: 0; top: 0; width: 758px; height: 236px;
    background: linear-gradient(180deg, #e9eff3 0%, #c7d6e0 30%, #7f8a5a 55%, #6f7448 72%, #8f9aa0 86%, #6d7a84 100%);
  }
  .site-url--lodge { right: 91px; top: 26px; text-align: right; }
  .lodge-name {
    position: absolute; right: 90px; top: 43px;
    font-family: "Arimo", Arial, sans-serif; font-size: 37px; font-weight: 700;
    letter-spacing: 1px; color: var(--ink);
  }
  .lodge-copy { position: absolute; left: 40px; width: 678px; text-align: center; }
  .welcome {
    top: 252px; font-family: "Quicksand", sans-serif; font-size: 16.5px;
    line-height: 18px; color: var(--ink-soft); letter-spacing: 0.4px; font-weight: 400;
  }
  .intro {
    top: 297px; font-family: "Quicksand", sans-serif; font-size: 12.8px;
    line-height: 15px; color: #333; letter-spacing: 0.5px; font-weight: 500;
  }
  .description { top: 342px; font-size: 11.5px; line-height: 15px; letter-spacing: 0.2px; }
  .description strong { font-weight: 700; }
  .contact-lead {
    top: 468px; font-family: "Quicksand", sans-serif; font-size: 21.5px;
    line-height: 26px; color: var(--ink); font-weight: 400;
  }
  .contact-phone { top: 492px; font-size: 19px; font-weight: 700; line-height: 24px; }
</style>
</head>
<body>
<main class="canvas">

  <section class="flyer flyer--yoga">
    <div class="lake-photo" role="img" aria-label="Woman in white meditating at the end of a wooden jetty over a calm, misty lake"></div>

    <h1 class="yoga-title">YOGA CLASSES ON A LAKE</h1>

    <div class="schedule" style="top:67px">
      <h3>Classes</h3>
    </div>
    <p class="schedule" style="top:97px">All classes are at Velino Retreat in the calm and relaxing lakeside studio unless different venue listed. Our one to one sessions are booked on a first come, first served basis and range from beginners and couple bookings to the more advanced sessions determined by your ability and preference.</p>

    <div class="schedule" style="top:185px">
      <h3>Monday</h3>
      <p>One to one bookings</p>
    </div>

    <div class="schedule" style="top:229px">
      <h3>Tuesday</h3>
      <p class="row">8-9 Hatha Yoga (STARTING SOON)</p>
      <p class="row">gentle asana class</p>
      <p class="row">10-11.15 Dru Yoga</p>
      <p class="row">19.00-20.00 Hatha Yoga (Ashcombe Memorial Hall)</p>
    </div>

    <div class="schedule" style="top:334px">
      <h3>Friday</h3>
      <p>10.00-11.15 Hatha Yoga</p>
    </div>

    <p class="schedule" style="top:385px; line-height:18px"><strong>DRU yoga</strong>&nbsp; - Brookfield community centre New dates to be arranged <span class="note">2014. 1pm to 4pm</span> <strong>£17</strong></p>

    <p class="site-url site-url--retreat">www.velinoretreat.co.uk</p>
    <p class="brand-name">VELINO RETREAT</p>

    <div class="info-band">
      <p class="tagline">A PEACEFUL &amp; TRANQUIL LAKESIDE<br>RETREAT IN THE HEART OF NORFOLK</p>
      <div class="booking">
        <p class="booking-lead">To book your space please Call</p>
        <p class="booking-phone">01632 960 418</p>
      </div>
    </div>
  </section>

  <section class="flyer flyer--lodge">
    <div class="lodge-photo" role="img" aria-label="Timber lodge and lakeside studio among trees on the edge of a lake under a pale sky"></div>
    <p class="site-url site-url--lodge">www.staysbycalderbrook.com</p>
    <h2 class="lodge-name">CALDERBROOK LODGE</h2>

    <p class="lodge-copy welcome">Welcome To The Start Of Your Getaway In The Heart<br>Of The English Countryside</p>
    <p class="lodge-copy intro">If you are looking to escape to the country for a short break, then our modern, spacious<br>cabin in the heart of Norfolk could be exactly what you are looking for</p>
    <p class="lodge-copy description">We are a family who rent out a cabin in the heart of the Norfolk countryside to offer people a chance to rest and relax! The cabin is surrounded by nature, with a picturesque lake and opportunities for walks through any number of the sleepy Norfolk villages. But don’t worry, the cabin is still outfitted with all the modern luxuries you would expect so you can relax in comfort! With room for up to 8 people, then we offer the perfect getaway for the whole family.<br><strong>We also offer retreats for any groups looking to really relax and enjoy a weekend of meditation and yoga in a studio suspended over the lake itself.</strong></p>

    <p class="lodge-copy contact-lead">Contact Us For More Information</p>
    <p class="lodge-copy contact-phone">Owen &amp; Mira's Mobile 07700 900 362</p>
  </section>

</main>
</body>
</html>
```